Salon and Spa Distributor Business Card

Need a business card. We are are distributor in the salon and spa industry. We identify with natural beauty. Need a card with:
Company Name: Petal Haven"
Title: "President & CEO"
Address
Company Phone number
email
website
Tag Line:" Natural Beauty for Every Salon"

Industry/Entity Type

Business

Contact Information for Business Card

Name: Lena Morcott
Title: "President & CEO"
Address: 317 Birchfield Ln, Oakvane, NJ 07481
Company Phone number: 800-463-9152
email: lenamorcott@petalhaven-example.com
website: www.petalhaven-example.com

Requirements
Should not have
• No black backgrounds

```html
<!DOCTYPE html>
<html lang="en">
<head>
<meta charset="utf-8">
<title>Petal Haven – Business Card</title>
<link href="https://fonts.googleapis.com/css2?family=Quicksand:wght@400;600;700&display=swap" rel="stylesheet">
<style>
  :root {
    --bg: #ecefea;
    --card: #ffffff;
    --green: #52d12c;
    --green-deep: #3bb51d;
    --brand-green: #2f9a22;
    --ink: #111111;
    --white: #ffffff;
  }
  * { margin: 0; padding: 0; box-sizing: border-box; }
  html, body {
    width: 1200px; height: 800px; overflow: hidden;
    background: var(--bg);
    font-family: "Quicksand", sans-serif;
  }
  .canvas { width: 1200px; height: 800px; position: relative; }
  .card {
    position: absolute; left: 285px;
    width: 630px; height: 360px;
    background: var(--card);
    box-shadow: 0 6px 20px rgba(0,0,0,0.12);
    overflow: hidden;
  }
  .card--back { top: 26px; }
  .card--front { top: 414px; }
  .card-shapes { position: absolute; inset: 0; }
  .band { fill: var(--green); }
  .band-shade { fill: var(--green-deep); }

  .brand {
    position: absolute;
    display: flex; align-items: center; gap: 14px;
    color: var(--brand-green);
    font-weight: 400;
    font-size: 44px;
    letter-spacing: 0.5px;
    white-space: nowrap;
  }
  .brand-dot {
    width: 40px; height: 40px; border-radius: 50%;
    background: var(--brand-green);
  }
  .card--back .brand { left: 170px; top: 120px; }
  .card--front .brand { right: 40px; top: 58px; }

  .tagline {
    position: absolute; left: 40px; bottom: 30px;
    color: var(--white);
    font-weight: 700; font-size: 30px;
    white-space: nowrap;
  }

  .person {
    position: absolute; left: 34px; top: 168px;
    color: var(--white);
  }
  .person-name { font-weight: 700; font-size: 30px; line-height: 1.1; }
  .person-title { font-weight: 600; font-size: 16px; }

  .contact-list {
    position: absolute; left: 300px; top: 236px;
    list-style: none;
    color: var(--ink);
    font-weight: 700; font-size: 14px;
  }
  .contact-list li {
    display: flex; align-items: center; gap: 8px;
    height: 22px;
    white-space: nowrap;
  }
  .contact-icon { width: 16px; height: 16px; flex: none; }
</style>
</head>
<body>
<div class="canvas">

  <section class="card card--back" aria-label="Card back">
    <svg class="card-shapes" viewBox="0 0 630 360" aria-hidden="true">
      <polygon class="band-shade" points="380,0 630,0 630,165" />
      <polygon class="band" points="410,0 630,0 630,140" />
      <polygon class="band" points="0,250 120,226 630,292 630,360 0,360" />
    </svg>
    <div class="brand"><span class="brand-dot"></span>Petal Haven</div>
    <p class="tagline">Natural Beauty for Every Salon</p>
  </section>

  <section class="card card--front" aria-label="Card front">
    <svg class="card-shapes" viewBox="0 0 630 360" aria-hidden="true">
      <polygon class="band" points="0,148 630,222 630,290 598,338 0,338" />
    </svg>
    <div class="brand"><span class="brand-dot"></span>Petal Haven</div>

    <div class="person">
      <p class="person-name">Lena Morcott</p>
      <p class="person-title">President &amp; CEO</p>
    </div>

    <ul class="contact-list">
      <li>
        <svg class="contact-icon" viewBox="0 0 16 16" aria-hidden="true"><circle cx="8" cy="8" r="8" fill="#111"/><path d="M5.5 4.5l1.5 0 .6 2-1 .8a5 5 0 0 0 2.1 2.1l.8-1 2 .6v1.5c-3.5.4-6.4-2.5-6-6z" fill="#fff"/></svg>
        800-463-9152
      </li>
      <li>
        <svg class="contact-icon" viewBox="0 0 16 16" aria-hidden="true"><circle cx="8" cy="8" r="8" fill="#111"/><rect x="4" y="5.2" width="8" height="5.6" fill="none" stroke="#fff" stroke-width="1.1"/><path d="M4 5.4l4 3 4-3" fill="none" stroke="#fff" stroke-width="1.1"/></svg>
        lenamorcott@petalhaven-example.com
      </li>
      <li>
        <svg class="contact-icon" viewBox="0 0 16 16" aria-hidden="true"><circle cx="8" cy="8" r="8" fill="#111"/><circle cx="8" cy="8" r="4" fill="none" stroke="#fff" stroke-width="1.1"/><path d="M4 8h8M8 4c-1.6 2.2-1.6 5.8 0 8M8 4c1.6 2.2 1.6 5.8 0 8" fill="none" stroke="#fff" stroke-width="0.9"/></svg>
        www.petalhaven-example.com
      </li>
      <li>
        <svg class="contact-icon" viewBox="0 0 16 16" aria-hidden="true"><circle cx="8" cy="8" r="8" fill="#111"/><path d="M8 3.6a3 3 0 0 0-3 3c0 2.2 3 5.6 3 5.6s3-3.4 3-5.6a3 3 0 0 0-3-3z" fill="#fff"/><circle cx="8" cy="6.6" r="1.1" fill="#111"/></svg>
        317 Birchfield Ln, Oakvane, NJ 07481
      </li>
    </ul>
  </section>

</div>
</body>
</html>
```